Quillmoor Farm Organic Flower Farm, Farmer Florist

I am a flower grower and florist, so I do everything from the field to the vase. I want to include my website, phone, email and instagram

```html
<!DOCTYPE html>
<html lang="en">
<head>
<meta charset="utf-8">
<title>Quillmoor Farm — Business Card</title>
<link href="https://fonts.googleapis.com/css2?family=Arimo:wght@400;500&display=swap" rel="stylesheet">
<style>
  :root {
    --backdrop: #e4e3e1;
    --paper: #f7f6f5;
    --wine: #6a2a33;
    --wine-deep: #4f1e25;
    --wine-light: #7d3540;
    --blush: #eea6a8;
    --blush-soft: #f3b9ba;
    --mist: #d9c3c5;
    --cream: #f6efef;
  }
  * { box-sizing: border-box; margin: 0; padding: 0; }
  html, body { width: 1200px; height: 801px; overflow: hidden; }
  body {
    background: var(--backdrop);
    font-family: "Arimo", Arial, sans-serif;
    position: relative;
  }
  .card {
    position: absolute;
    top: 246px;
    width: 540px;
    height: 309px;
    overflow: hidden;
    box-shadow: 0 6px 18px rgba(0,0,0,0.18);
  }
  .card--contact { left: 40px; background: var(--paper); }
  .card--brand {
    left: 620px;
    background: radial-gradient(ellipse at 60% 40%, var(--wine-light), var(--wine) 55%, var(--wine-deep));
  }

  /* contact side */
  .contact-band {
    position: absolute; left: 0; right: 0; top: 138px; bottom: 0;
    background: linear-gradient(180deg, var(--wine), var(--wine-deep));
  }
  .art { position: absolute; }
  .art--barn {
    left: 150px; top: 30px; width: 170px; height: 108px;
    background: linear-gradient(180deg, rgba(238,166,168,0.55), rgba(106,42,51,0.6));
    border-radius: 8px 8px 0 0;
  }
  .art--stems-right {
    right: 14px; top: 18px; width: 170px; height: 120px;
    background: linear-gradient(160deg, rgba(106,42,51,0.12), rgba(106,42,51,0.45));
    border-radius: 8px 8px 0 0;
  }
  .art--stems-left {
    left: 14px; top: 60px; width: 120px; height: 78px;
    background: linear-gradient(200deg, rgba(106,42,51,0.1), rgba(106,42,51,0.4));
    border-radius: 8px 8px 0 0;
  }
  .person {
    position: absolute; left: 32px; top: 222px;
  }
  .person__name {
    color: var(--blush); font-size: 22px; font-weight: 500; letter-spacing: 0.5px;
  }
  .person__role {
    color: var(--mist); font-size: 14px; margin-top: 4px; text-align: right;
  }
  .divider {
    position: absolute; left: 262px; top: 160px; width: 1px; height: 130px;
    background: var(--mist);
  }
  .contacts {
    position: absolute; left: 282px; top: 166px; list-style: none;
  }
  .contacts li {
    display: flex; align-items: center; gap: 10px;
    color: var(--mist); font-size: 15px; height: 30px;
  }
  .contacts svg { width: 14px; height: 14px; flex: none; }

  /* brand side */
  .brand {
    position: absolute; right: 36px; top: 56px;
    display: flex; flex-direction: column; align-items: center;
  }
  .brand__row { display: flex; align-items: center; gap: 12px; }
  .brand__mark { width: 18px; height: 18px; background: var(--blush); }
  .brand__name {
    color: var(--cream); font-size: 34px; font-weight: 400; letter-spacing: 3px;
  }
  .brand__tagline {
    color: var(--blush); font-size: 17px; letter-spacing: 1px; margin-top: 8px;
  }
  .brand__est {
    color: var(--cream); font-size: 11px; letter-spacing: 3px; margin-top: 6px;
  }
  .art--bloom {
    left: 30px; bottom: 0; width: 480px; height: 150px;
    background: linear-gradient(70deg, rgba(79,30,37,0.6), rgba(200,120,125,0.55) 60%, rgba(238,166,168,0.75));
    border-radius: 12px 12px 0 0;
  }
</style>
</head>
<body>
  <section class="card card--contact" aria-label="Card contact side">
    <div class="contact-band"></div>
    <div class="art art--stems-right" role="img" aria-label="Wildflower stems illustration"></div>
    <div class="art art--stems-left" role="img" aria-label="Wildflower sprigs illustration"></div>
    <div class="art art--barn" role="img" aria-label="Barn illustration with a bird on the roof"></div>
    <div class="person">
      <p class="person__name">MARLOW TENNEY</p>
      <p class="person__role">Manager</p>
    </div>
    <div class="divider"></div>
    <ul class="contacts">
      <li>
        <svg viewBox="0 0 14 14"><path d="M3 1l2 3-1 1.5c.8 1.7 2 2.9 3.5 3.5L9 8l3 2-1 2.5C6 12 2 8 1.5 3z" fill="var(--mist)"/></svg>
        555-014-2730
      </li>
      <li>
        <svg viewBox="0 0 14 14"><rect x="1" y="3" width="12" height="8" fill="none" stroke="var(--mist)" stroke-width="1.4"/><path d="M1 3l6 5 6-5" fill="none" stroke="var(--mist)" stroke-width="1.4"/></svg>
        info@quillmoor.com
      </li>
      <li>
        <svg viewBox="0 0 14 14"><circle cx="7" cy="7" r="5.5" fill="none" stroke="var(--mist)" stroke-width="1.4"/><path d="M1.5 7h11M7 1.5c-3 3-3 8 0 11M7 1.5c3 3 3 8 0 11" fill="none" stroke="var(--mist)" stroke-width="1"/></svg>
        www.quillmoor.com
      </li>
      <li>
        <svg viewBox="0 0 14 14"><rect x="2" y="2" width="10" height="10" fill="var(--mist)"/></svg>
        @quillmoor
      </li>
    </ul>
  </section>

  <section class="card card--brand" aria-label="Card brand side">
    <div class="brand">
      <div class="brand__row">
        <span class="brand__mark"></span>
        <span class="brand__name">QUILLMOOR</span>
      </div>
      <p class="brand__tagline">organic flower farm</p>
      <p class="brand__est">EST. 2019</p>
    </div>
    <div class="art art--bloom" role="img" aria-label="Large embossed flowering stem illustration"></div>
  </section>
</body>
</html>
```